Property Service business needs a cool business card

Looking for an eloquent and unique business card using the logo and colours attached as uploaded files.

Target Market(s)

Body corporates, real estate agents, building managers

Industry/Entity Type

Business

Contact Information for Business Card

- Kelvo Logo
- Construction * Maintenance * Remedial

- Ned Pirrick
- Business Manager

- Ph 0417586043
- P.O Box 514 South Melbourne Vic 3090
- Email ned@kelvo.com
- Website www.kelvopropertyservices.com.au

Requirements
Must have
• Clean and fresh look, colours must be vibrant!
Nice to have
• unique features
Should not have
• Should not be overcrowded

```html
<!DOCTYPE html>
<html lang="en">
<head>
<meta charset="utf-8">
<title>Kelvo Property Services – Business Cards</title>
<link rel="stylesheet" href="https://fonts.googleapis.com/css2?family=Open+Sans:ital,wght@0,400;0,600;0,700;1,400&display=swap">
<style>
  :root {
    --backdrop: #8e8e8e;
    --card-white: #f2f2f2;
    --brand-blue: #0b4f9c;
    --brand-green: #8cc63f;
    --text-grey: #4a4a4a;
    --rule-grey: #b5b5b5;
    --white: #ffffff;
  }
  * { margin: 0; padding: 0; box-sizing: border-box; }
  html, body { width: 1200px; height: 750px; overflow: hidden; }
  body {
    background: var(--backdrop);
    font-family: "Open Sans", Arial, sans-serif;
    position: relative;
  }
  .card {
    position: absolute;
    width: 492px;
    height: 281px;
    border-radius: 13px;
    overflow: hidden;
  }
  .card--front { background: var(--card-white); top: 72px; }
  .card--ned { left: 84px; }
  .card--liam { left: 635px; }
  .card--back { background: var(--brand-blue); left: 360px; top: 398px; }

  .brand {
    position: absolute;
    left: 22px;
    top: 22px;
    display: flex;
    align-items: center;
    gap: 14px;
  }
  .brand__mark {
    width: 52px;
    height: 52px;
    background: var(--brand-blue);
  }
  .brand__name {
    font-size: 40px;
    font-weight: 600;
    color: var(--brand-blue);
    line-height: 1;
  }

  .holder {
    position: absolute;
    right: 269px;
    top: 148px;
    text-align: right;
  }
  .holder__name {
    font-size: 17px;
    font-weight: 700;
    color: var(--brand-blue);
    line-height: 1.3;
  }
  .holder__role {
    font-size: 13px;
    color: var(--brand-green);
    margin-top: 4px;
  }
  .divider {
    position: absolute;
    left: 241px;
    top: 140px;
    width: 1px;
    height: 56px;
    background: var(--rule-grey);
  }
  .contact {
    position: absolute;
    left: 262px;
    top: 136px;
    font-size: 12px;
    color: var(--text-grey);
    line-height: 16px;
  }
  .contact__address { margin-bottom: 6px; }
  .contact__line { margin-bottom: 4px; }
  .contact__label { color: var(--brand-blue); font-weight: 700; margin-right: 3px; }

  .web-band {
    position: absolute;
    left: 0;
    right: 0;
    top: 242px;
    height: 32px;
    border-top: 2px solid var(--brand-green);
    border-bottom: 2px solid var(--brand-green);
    background: var(--card-white);
    padding: 1px 0;
  }
  .web-band__fill {
    height: 100%;
    background: var(--brand-blue);
    color: var(--white);
    font-size: 13px;
    font-style: italic;
    letter-spacing: 1.2px;
    text-align: center;
    line-height: 26px;
  }

  .back__name {
    position: absolute;
    left: 24px;
    top: 82px;
    font-size: 70px;
    font-weight: 400;
    color: var(--white);
    line-height: 1;
  }
  .back__subtitle {
    position: absolute;
    left: 25px;
    top: 152px;
    font-size: 22px;
    color: var(--white);
    letter-spacing: 0.5px;
  }
  .back__services {
    position: absolute;
    left: 25px;
    top: 181px;
    font-size: 13.5px;
    color: var(--brand-green);
  }
  .back__services .dot { font-size: 11px; margin: 0 3px; }
</style>
</head>
<body>

  <section class="card card--front card--ned">
    <div class="brand"><span class="brand__mark"></span><span class="brand__name">Kelvo</span></div>
    <div class="holder">
      <div class="holder__name">Ned Pirrick</div>
      <div class="holder__role">Business Manager</div>
    </div>
    <div class="divider"></div>
    <div class="contact">
      <div class="contact__address">Level 2, 14 Harbour Rd<br>Melbourne Vic 3006</div>
      <div class="contact__line"><span class="contact__label">T :</span>04 1758 6043</div>
      <div class="contact__line"><span class="contact__label">E :</span>ned@kelvo.com</div>
    </div>
    <div class="web-band"><div class="web-band__fill">www.kelvopropertyservices.com.au</div></div>
  </section>

  <section class="card card--front card--liam">
    <div class="brand"><span class="brand__mark"></span><span class="brand__name">Kelvo</span></div>
    <div class="holder">
      <div class="holder__name">Liam Corvell</div>
      <div class="holder__role">Operations Manager</div>
    </div>
    <div class="divider"></div>
    <div class="contact">
      <div class="contact__address">Level 2, 14 Harbour Rd<br>Melbourne Vic 3006</div>
      <div class="contact__line"><span class="contact__label">T :</span>03 9521 4760</div>
      <div class="contact__line"><span class="contact__label">E :</span>liam@kelvo.com.au</div>
    </div>
    <div class="web-band"><div class="web-band__fill">www.kelvopropertyservices.com.au</div></div>
  </section>

  <section class="card card--back">
    <div class="back__name">Kelvo</div>
    <div class="back__subtitle">Property Services</div>
    <div class="back__services">Project Management <span class="dot">●</span>Maintenance <span class="dot">●</span>Remedial</div>
  </section>

</body>
</html>
```